Business Card Design Project

I need some business cards with the logo you did for us (attached)
I am looking for a coulourful yet serious business card

We do market research
on the back I want the logo

on the front my name : Corinne Valdessac
position : Manager
address : Brume Analytica Sarl - 27 Rue des tanneurs
1847 Glarency - Switzerland
corinne.valdessac@brumeanalytica.ch
Tel : +4122 934 07 58
Mob France :+33 671 42 8356
Mob Italy +39 347 520 8163

The tree of the logo could also be used alone

THE BACKGROUND COLOR ON THE FRONT HAS TO BE WHITE, ON THE BACK YU CAN TRY OHER COLOUR BUT HOMOGENEOUS (NOT EXPENSIVE TO PRINT)

Target Market(s)

multinational companies or other market research companies

Industry/Entity Type

Market Research

Requirements
Must have
• logo on the back
and all the info above

```html
<!DOCTYPE html>
<html lang="en">
<head>
<meta charset="utf-8">
<title>Brume Analytica – Business Card</title>
<link rel="stylesheet" href="https://fonts.googleapis.com/css2?family=Roboto+Condensed:wght@300;400;700&display=swap">
<style>
  :root {
    --page-bg: #ebe7e2;
    --card-red: #c4283f;
    --card-red-light: #d8435a;
    --card-red-dark: #a81e33;
    --card-white: #ffffff;
    --ink-red: #b5213a;
    --ink-grey: #6f6f72;
    --ink-light: #9a9a9e;
    --logo-white: #ffffff;
    --shadow: rgba(60, 40, 20, 0.22);
  }
  * { box-sizing: border-box; margin: 0; padding: 0; }
  html, body {
    width: 1200px;
    height: 968px;
    overflow: hidden;
  }
  body {
    background: var(--page-bg);
    font-family: "Roboto Condensed", Arial, sans-serif;
    position: relative;
  }
  .card {
    position: absolute;
    left: 320px;
    width: 560px;
    height: 320px;
    border-radius: 4px;
    box-shadow: 0 10px 30px var(--shadow);
    overflow: hidden;
  }
  .card--back {
    top: 90px;
    background: linear-gradient(135deg, var(--card-red-light) 0%, var(--card-red) 50%, var(--card-red-dark) 100%);
  }
  .card__pattern {
    position: absolute;
    inset: 0;
    background: radial-gradient(ellipse at 60% 35%, rgba(255,255,255,0.12) 0%, rgba(255,255,255,0.04) 55%, rgba(255,255,255,0) 80%);
  }
  .brand {
    position: absolute;
    left: 50%;
    top: 50%;
    transform: translate(-50%, -50%);
    display: flex;
    align-items: center;
    gap: 14px;
  }
  .brand__dot {
    width: 34px;
    height: 34px;
    border-radius: 50%;
    background: var(--logo-white);
  }
  .brand__name {
    color: var(--logo-white);
    font-size: 40px;
    font-weight: 400;
    letter-spacing: 0.5px;
    white-space: nowrap;
  }
  .card--front {
    top: 520px;
    background: var(--card-white);
    padding: 46px 50px;
  }
  .contact__name {
    color: var(--ink-red);
    font-size: 26px;
    font-weight: 700;
  }
  .contact__role {
    color: var(--ink-grey);
    font-size: 15px;
    font-weight: 400;
    margin-top: 4px;
  }
  .contact__address {
    margin-top: 30px;
    color: var(--ink-grey);
    font-size: 14px;
    font-weight: 300;
    line-height: 1.5;
    font-style: normal;
  }
  .contact__lines {
    position: absolute;
    right: 50px;
    bottom: 46px;
    list-style: none;
    color: var(--ink-grey);
    font-size: 14px;
    font-weight: 300;
    line-height: 1.6;
    text-align: right;
  }
  .contact__label { color: var(--ink-light); }
</style>
</head>
<body>
  <section class="card card--back" aria-label="Card back">
    <div class="card__pattern" role="img" aria-label="Faint tone-on-tone swirl pattern"></div>
    <div class="brand">
      <span class="brand__dot"></span>
      <span class="brand__name">brume analytica</span>
    </div>
  </section>

  <section class="card card--front" aria-label="Card front">
    <h1 class="contact__name">Corinne Valdessac</h1>
    <p class="contact__role">Manager</p>
    <address class="contact__address">
      Brume Analytica Sarl<br>
      27 Rue des tanneurs<br>
      1847 Glarency – Switzerland
    </address>
    <ul class="contact__lines">
      <li>corinne.valdessac@brumeanalytica.ch</li>
      <li><span class="contact__label">Tel</span> +4122 934 07 58</li>
      <li><span class="contact__label">Mob France</span> +33 671 42 8356</li>
      <li><span class="contact__label">Mob Italy</span> +39 347 520 8163</li>
    </ul>
  </section>
</body>
</html>
```